We are looking to create a graphic that will be used in Facebook posts each week to show the daily Porchlight Report. Attached is an example of what we are looking for. We need to be able to update the forecast. So we will need hi-res vector files. The graphics need to represent the level of mosquito activity: SLIGHT, AVERAGE, INTENSE, EXTREME

```html
<!DOCTYPE html>
<html lang="en">
<head>
<meta charset="utf-8">
<title>Porchlight Report – Weekly Activity</title>
<link href="https://fonts.googleapis.com/css2?family=Poppins:wght@300;400;500;800&display=swap" rel="stylesheet">
<style>
  :root{
    --grass-light:#b9dc6e;
    --grass-mid:#7cbf3a;
    --grass-deep:#3f8a1c;
    --grass-dark:#2c6a12;
    --white:#ffffff;
    --ink:#1c1c1c;
    --card-fill:rgba(236,246,220,0.55);
    --card-edge:rgba(255,255,255,0.55);
    --gauge-green:#2fd91f;
    --gauge-yellow:#f5b800;
    --gauge-orange:#ea4b1f;
    --gauge-red:#c42a1e;
    --gauge-maroon:#7a1a14;
    --gauge-track:#e6e6e6;
    --badge-fill:#b3261e;
  }
  *{box-sizing:border-box;margin:0;padding:0}
  html,body{width:1200px;height:674px;overflow:hidden}
  body{font-family:"Poppins",sans-serif;color:var(--ink)}
  .poster{position:relative;width:1200px;height:674px;overflow:hidden}
  .backdrop{
    position:absolute;inset:0;
    background:
      radial-gradient(ellipse 70% 45% at 50% 18%, rgba(214,236,150,0.75), transparent 70%),
      linear-gradient(180deg, var(--grass-light) 0%, var(--grass-mid) 40%, var(--grass-deep) 75%, var(--grass-dark) 100%);
  }
  .region{
    position:absolute;left:0;right:0;top:158px;
    text-align:center;color:var(--white);
    font-weight:300;font-size:33px;letter-spacing:10px;line-height:1;
    padding-left:10px;
  }
  .headline{
    position:absolute;left:0;right:0;top:193px;
    text-align:center;color:var(--white);
    font-weight:800;font-size:68px;line-height:1;letter-spacing:-0.5px;
  }
  .week{
    position:absolute;left:82px;top:302px;
    display:flex;gap:18px;list-style:none;
  }
  .day-card{
    width:131px;height:197px;border-radius:16px;
    background:var(--card-fill);
    border:1px solid var(--card-edge);
    backdrop-filter:blur(6px);
    text-align:center;position:relative;
  }
  .day-name{position:absolute;top:22px;left:0;right:0;font-size:15px;line-height:1}
  .day-date{position:absolute;top:43px;left:0;right:0;font-size:15px;line-height:1}
  .gauge{position:absolute;left:27px;top:75px;width:77px;height:77px}
  .level{position:absolute;top:165px;left:0;right:0;font-size:12.5px;font-weight:500;line-height:1;letter-spacing:0.3px}
</style>
</head>
<body>
<svg width="0" height="0" style="position:absolute" aria-hidden="true">
  <defs>
    <g id="ring-base" fill="none" stroke-width="7.5">
      <circle cx="40" cy="40" r="34" stroke="var(--gauge-track)"/>
      <circle cx="40" cy="40" r="34" pathLength="360" stroke-dasharray="60 300" transform="rotate(120 40 40)" stroke="var(--gauge-green)"/>
      <circle cx="40" cy="40" r="34" pathLength="360" stroke-dasharray="60 300" transform="rotate(180 40 40)" stroke="var(--gauge-yellow)"/>
    </g>
    <g id="ring-mid" fill="none" stroke-width="7.5">
      <circle cx="40" cy="40" r="34" pathLength="360" stroke-dasharray="60 300" transform="rotate(240 40 40)" stroke="var(--gauge-orange)"/>
      <circle cx="40" cy="40" r="34" pathLength="360" stroke-dasharray="60 300" transform="rotate(300 40 40)" stroke="var(--gauge-red)"/>
    </g>
    <g id="ring-top" fill="none" stroke-width="7.5">
      <circle cx="40" cy="40" r="34" pathLength="360" stroke-dasharray="60 300" transform="rotate(0 40 40)" stroke="var(--gauge-maroon)"/>
    </g>
    <g id="gauge-slight"><use href="#ring-base"/></g>
    <g id="gauge-intense"><use href="#ring-base"/><use href="#ring-mid"/></g>
    <g id="gauge-extreme"><use href="#ring-base"/><use href="#ring-mid"/><use href="#ring-top"/></g>
    <g id="insect-badge"><circle cx="40" cy="40" r="11" fill="var(--badge-fill)" opacity="0.85"/></g>
  </defs>
</svg>

<main class="poster">
  <div class="backdrop" role="img" aria-label="Close-up photograph of fresh green grass with dew drops"></div>
  <p class="region">GREATER LARKHAVEN</p>
  <h1 class="headline">PORCHLIGHT REPORT</h1>

  <ul class="week">
    <li class="day-card"><p class="day-name">Thu</p><p class="day-date">7/21</p>
      <svg class="gauge" viewBox="0 0 80 80"><use href="#gauge-extreme"/><g role="img" aria-label="Mosquito icon"><use href="#insect-badge"/></g></svg>
      <p class="level">EXTREME</p></li>
    <li class="day-card"><p class="day-name">Fri</p><p class="day-date">7/22</p>
      <svg class="gauge" viewBox="0 0 80 80"><use href="#gauge-intense"/><g role="img" aria-label="Mosquito icon"><use href="#insect-badge"/></g></svg>
      <p class="level">INTENSE</p></li>
    <li class="day-card"><p class="day-name">Sat</p><p class="day-date">7/23</p>
      <svg class="gauge" viewBox="0 0 80 80"><use href="#gauge-intense"/><g role="img" aria-label="Mosquito icon"><use href="#insect-badge"/></g></svg>
      <p class="level">INTENSE</p></li>
    <li class="day-card"><p class="day-name">Sun</p><p class="day-date">7/24</p>
      <svg class="gauge" viewBox="0 0 80 80"><use href="#gauge-slight"/><g role="img" aria-label="Mosquito icon"><use href="#insect-badge"/></g></svg>
      <p class="level">SLIGHT</p></li>
    <li class="day-card"><p class="day-name">Mon</p><p class="day-date">7/25</p>
      <svg class="gauge" viewBox="0 0 80 80"><use href="#gauge-extreme"/><g role="img" aria-label="Mosquito icon"><use href="#insect-badge"/></g></svg>
      <p class="level">EXTREME</p></li>
    <li class="day-card"><p class="day-name">Tue</p><p class="day-date">7/26</p>
      <svg class="gauge" viewBox="0 0 80 80"><use href="#gauge-slight"/><g role="img" aria-label="Mosquito icon"><use href="#insect-badge"/></g></svg>
      <p class="level">SLIGHT</p></li>
    <li class="day-card"><p class="day-name">Wed</p><p class="day-date">7/27</p>
      <svg class="gauge" viewBox="0 0 80 80"><use href="#gauge-intense"/><g role="img" aria-label="Mosquito icon"><use href="#insect-badge"/></g></svg>
      <p class="level">INTENSE</p></li>
  </ul>
</main>
</body>
</html>
```